Remedial massage therapist or clinical look

I would like a plain white or light colour background with front view of a musculoskeletal human body on the from on the left hand side, with Mira Dostane remedial and sports massage therapist. On the back I want the back view of the musculoskeletal body on the left side with Mira Dostane remedial and sports massage therapist, my contact details and appointment time and date. The colour of writing can be the same or close colour to the musculoskeletal body.
I don't want it to look to busy but also don't want it to be to plain,

Industry/Entity Type

Massage

Contact Information for Business Card

Mira Dostane
Remedial and Sports Massage Therapist
Contact number: 0481536207
Email: dostanemira41@quillmark.net

```html
<!DOCTYPE html>
<html lang="en">
<head>
<meta charset="utf-8">
<title>Mira Dostane – Remedial and Sports Massage Therapist</title>
<link rel="stylesheet" href="https://fonts.googleapis.com/css2?family=Noto+Serif:wght@400&display=swap">
<style>
  :root {
    --paper: #fdfcf9;
    --teal: #48a9a8;
    --dots: #9a9792;
    --mint: #a6f2d6;
    --mint-soft: #c9f7e6;
    --ribbon: #efeadf;
    --ribbon-soft: #f7f4ee;
  }
  html, body {
    margin: 0;
    padding: 0;
    overflow: hidden;
    background: var(--paper);
  }
  .card {
    position: relative;
    width: 694px;
    height: 1200px;
    overflow: hidden;
    background: var(--paper);
    font-family: "Noto Serif", "DejaVu Serif", serif;
  }
  .ribbon-backdrop {
    position: absolute;
    left: 327px;
    top: 0;
    width: 367px;
    height: 1200px;
    background:
      radial-gradient(ellipse 60% 30% at 70% 20%, var(--ribbon) 0%, transparent 70%),
      radial-gradient(ellipse 55% 35% at 40% 75%, var(--ribbon) 0%, transparent 70%),
      linear-gradient(180deg, var(--ribbon-soft) 0%, var(--paper) 45%, var(--ribbon-soft) 100%);
  }
  .anatomy-figure {
    position: absolute;
    left: 6px;
    top: 62px;
    width: 244px;
    height: 1048px;
    border-radius: 110px 40px 60px 90px;
    background: linear-gradient(180deg, var(--mint) 0%, var(--mint-soft) 55%, var(--mint) 100%);
  }
  .divider {
    position: absolute;
  }
  .divider--vertical {
    left: 266px;
    top: 62px;
    width: 4px;
    height: 1038px;
  }
  .divider--horizontal {
    left: 268px;
    width: 382px;
    height: 4px;
  }
  .divider--upper { top: 520px; }
  .divider--lower { top: 697px; }
  .therapist-name {
    position: absolute;
    left: 316px;
    top: 330px;
    margin: 0;
    font-size: 72px;
    font-weight: 400;
    line-height: 87px;
    color: var(--teal);
  }
  .therapist-role {
    position: absolute;
    left: 316px;
    top: 538px;
    margin: 0;
    font-size: 36px;
    line-height: 46px;
    color: var(--teal);
  }
</style>
</head>
<body>
  <main class="card">
    <div class="ribbon-backdrop" role="img" aria-label="Soft flowing beige ribbon waves"></div>
    <div class="anatomy-figure" role="img" aria-label="Front view illustration of the human musculoskeletal body in mint green"></div>

    <svg class="divider divider--vertical" viewBox="0 0 4 1038" aria-hidden="true">
      <line x1="2" y1="2" x2="2" y2="1036" stroke="var(--dots)" stroke-width="3.4" stroke-linecap="round" stroke-dasharray="0 9"/>
    </svg>
    <svg class="divider divider--horizontal divider--upper" viewBox="0 0 382 4" aria-hidden="true">
      <line x1="2" y1="2" x2="380" y2="2" stroke="var(--dots)" stroke-width="3.4" stroke-linecap="round" stroke-dasharray="0 9"/>
    </svg>
    <svg class="divider divider--horizontal divider--lower" viewBox="0 0 382 4" aria-hidden="true">
      <line x1="2" y1="2" x2="380" y2="2" stroke="var(--dots)" stroke-width="3.4" stroke-linecap="round" stroke-dasharray="0 9"/>
    </svg>

    <h1 class="therapist-name">Mira<br>Dostane</h1>
    <p class="therapist-role">Remedial and<br>Sports Massage<br>Therapist</p>
  </main>
</body>
</html>
```